Brightmoor Card Company Business Cards

We are a trading card store with Zorblix, sports and other TCG cards, we need a business card design that encompasses a clean cut, modern style with a retro flare. website is brightmoorcardco.com for reference. Can utilize a comic book era feel or a more modern outdoor feel to utilize the "Pacific Northwest" elements of tress, mountains, etc.

Industry/Entity Type

Trading cards and collectibles

Contact Information for Business Card

business name, email address, phone number, name, owner job title

Font styles to use
Sans Serif

```html
<!DOCTYPE html>
<html lang="en">
<head>
<meta charset="utf-8">
<title>Brightmoor Card Company – Business Cards</title>
<link rel="stylesheet" href="https://fonts.googleapis.com/css2?family=Open+Sans:wght@400;600;700&display=swap">
<style>
  :root {
    --backdrop: #cfcfcd;
    --card-white: #f7f7f6;
    --card-grey: #6a6a6c;
    --ink-grey: #5e5e60;
    --emboss-grey: #58585a;
    --accent-teal: #1ba9d6;
    --edge-teal: #1597b8;
    --white: #ffffff;
  }
  * { margin: 0; padding: 0; box-sizing: border-box; }
  html, body { width: 1200px; height: 810px; overflow: hidden; }
  body {
    background: var(--backdrop);
    font-family: "Open Sans", sans-serif;
    position: relative;
  }
  .card {
    position: absolute;
    width: 525px;
    height: 300px;
    border-bottom: 4px solid var(--edge-teal);
    box-shadow: 0 6px 18px rgba(0,0,0,0.18);
  }
  .card-front { left: 50px; top: 255px; background: var(--card-white); }
  .card-back  { left: 625px; top: 255px; background: var(--card-grey); }

  .front-brand {
    position: absolute;
    right: 38px;
    top: 36px;
    display: flex;
    align-items: center;
    gap: 8px;
    color: var(--ink-grey);
    font-weight: 700;
    font-size: 15px;
    letter-spacing: 0.04em;
    text-transform: uppercase;
  }
  .brand-mark {
    width: 14px; height: 14px;
    border-radius: 50%;
    background: var(--accent-teal);
  }
  .contact-block {
    position: absolute;
    left: 40px;
    bottom: 38px;
  }
  .person-name {
    color: var(--accent-teal);
    font-weight: 700;
    font-size: 22px;
    line-height: 1.1;
  }
  .person-title {
    color: var(--ink-grey);
    font-size: 14px;
    margin-bottom: 14px;
  }
  .contact-list { list-style: none; }
  .contact-list li {
    display: flex;
    align-items: center;
    gap: 9px;
    color: var(--ink-grey);
    font-size: 14px;
    line-height: 1.5;
  }
  .contact-icon { width: 12px; height: 12px; flex: none; }

  .back-brand {
    position: absolute;
    left: 0; right: 0;
    top: 92px;
    text-align: center;
    color: var(--emboss-grey);
    font-weight: 700;
    font-size: 30px;
    letter-spacing: 0.05em;
    text-transform: uppercase;
    line-height: 1.15;
  }
  .back-web {
    position: absolute;
    left: 0; right: 0;
    bottom: 48px;
    text-align: center;
    color: var(--white);
    font-size: 16px;
    letter-spacing: 0.02em;
  }
  .back-web strong { font-weight: 700; }
</style>
</head>
<body>
  <section class="card card-front" aria-label="Business card front">
    <div class="front-brand"><span class="brand-mark"></span>Brightmoor Card Company</div>
    <div class="contact-block">
      <p class="person-name">Daniel Whitaker</p>
      <p class="person-title">Managing Director</p>
      <ul class="contact-list">
        <li>
          <svg class="contact-icon" viewBox="0 0 12 12" aria-hidden="true"><path d="M2.5 1h2l1 3-1.3 1a6 6 0 0 0 2.8 2.8L8 6.5l3 1v2c0 .8-.7 1.5-1.5 1.5A9 9 0 0 1 1 2.5C1 1.7 1.7 1 2.5 1z" fill="var(--accent-teal)"/></svg>
          210.555.0147
        </li>
        <li>
          <svg class="contact-icon" viewBox="0 0 12 12" aria-hidden="true"><rect x="0.5" y="2" width="11" height="8" rx="1" fill="var(--accent-teal)"/><path d="M1 2.8l5 3.7 5-3.7" stroke="var(--white)" stroke-width="1" fill="none"/></svg>
          info@brightmoorcardco.com
        </li>
        <li>
          <svg class="contact-icon" viewBox="0 0 12 12" aria-hidden="true"><circle cx="6" cy="6" r="5.5" fill="var(--accent-teal)"/><path d="M1 6h10M6 .5c-2 2.5-2 8.5 0 11M6 .5c2 2.5 2 8.5 0 11" stroke="var(--white)" stroke-width=".8" fill="none"/></svg>
          www.brightmoorcardco.com
        </li>
      </ul>
    </div>
  </section>

  <section class="card card-back" aria-label="Business card back">
    <p class="back-brand">Brightmoor<br>Card Company</p>
    <p class="back-web">www.<strong>brightmoorcardco</strong>.com</p>
  </section>
</body>
</html>
```